" A Trilo Sistemas é uma empresa que desenvolve sistemas de monitoramento remoto, telemetria via satélite, telecontrole, automaçao, rastreamento de veículos e etc.. Trata-se de uma empresa moderna e jovem, com uma linguagem de comunicaçao moderna e descontraída, sem perder a seriedade. Temos dois segmentos: Corporativo e Varejo. No corporativo, prestamos serviço para grandes empresas como Pedra Alta Minérios por exemplo.Já no varejo atendemos pessoas fisicas ou pequenas empresas. "

```html
<!DOCTYPE html>
<html lang="pt-BR">
<head>
<meta charset="utf-8">
<title>Trilo Sistemas</title>
<link href="https://fonts.googleapis.com/css2?family=Cabin:wght@400;700&family=Open+Sans:wght@400;700&display=swap" rel="stylesheet">
<style>
:root{
  --orange:#e5772f;
  --orange-dark:#d9621f;
  --blue:#3e6f8c;
  --navy:#1f4862;
  --gray:#8a8a8a;
  --light:#f1f1f1;
  --white:#fff;
}
*{margin:0;padding:0;box-sizing:border-box}
html,body{width:1200px;height:1200px;overflow:hidden;background:#fff}
body{position:relative;font-family:"Open Sans",sans-serif;color:var(--gray)}
.page{position:absolute;left:460px;top:0;width:280px;height:1200px;background:#fff;overflow:hidden}
.abs{position:absolute}
.title{font-family:"Cabin",sans-serif;font-weight:700;text-align:center;letter-spacing:.3px}

.hero{left:0;top:0;width:280px;height:156px;background:linear-gradient(160deg,#dfe3e6 0%,#aab4bb 45%,#5b6770 80%,#3f4a52 100%)}
.login{left:242px;top:4px;width:30px;height:9px;background:var(--orange);color:#fff;font-size:4.5px;line-height:9px;text-align:center;font-weight:700}
.hero-banner{left:8px;top:118px;width:118px;padding:3px 5px;background:var(--orange);color:#fff;font-size:5px;line-height:6.5px;font-weight:700;text-transform:uppercase}

.nav{left:0;top:156px;width:280px;height:40px;background:var(--orange-dark);display:flex;align-items:center}
.brand{margin-left:10px;width:84px;color:#fff;font-family:"Cabin",sans-serif;font-weight:700;font-size:10px;white-space:nowrap}
.nav-home{width:22px;height:40px;background:var(--blue);color:#fff;font-size:4.5px;display:flex;align-items:flex-end;justify-content:center;padding-bottom:6px}
.nav-links{display:flex;gap:9px;margin-left:9px;color:#fff;font-size:4.8px;white-space:nowrap}

.features{left:8px;top:206px;width:264px;display:flex;justify-content:space-between}
.feature{width:82px}
.feature .thumb{position:relative;height:66px}
.feature .tag{position:absolute;right:3px;bottom:3px;background:var(--orange);color:#fff;font-size:4px;padding:1px 3px}
.feature p{margin-top:4px;font-size:4px;line-height:5.2px}

.sol-title{left:0;top:322px;width:280px;color:var(--blue);font-size:15px}
.sol-text{left:40px;top:342px;width:200px;text-align:center;font-size:5.6px;line-height:7.5px;color:var(--orange)}
.sol-text b{color:var(--orange-dark)}
.device{left:74px;top:388px;width:150px;height:100px;background:#e3e6e8;border-radius:3px}
.device .screen{position:absolute;left:6px;top:6px;width:138px;height:78px;background:linear-gradient(180deg,#b9c3cb,#5e6a73 60%,#3b434a)}
.device .stand{position:absolute;left:60px;top:92px;width:30px;height:8px;background:#c9cdd0}
.tablet{left:60px;top:456px;width:24px;height:32px;background:linear-gradient(#cfd4d8,#8d979e);border-radius:2px}
.dots{left:130px;top:528px;display:flex;gap:3px}
.dots span{width:4px;height:4px;border-radius:50%;background:#cfcfcf}
.dots span:first-child{background:var(--gray)}
.btn{background:var(--orange);color:#fff;font-weight:700;font-size:5px;text-align:center;text-transform:uppercase}
.sol-btn{left:116px;top:541px;width:48px;height:12px;line-height:12px}

.segments{left:0;top:574px;width:280px;height:182px;background:var(--blue);color:#fff}
.seg-title{left:0;top:12px;width:280px;font-size:15px}
.seg-text{left:50px;top:36px;width:180px;text-align:center;font-size:5.6px;line-height:7.5px}
.seg-items{left:22px;top:88px;width:236px;display:flex;justify-content:space-between}
.seg-item{width:64px;text-align:center;font-size:6px;font-weight:700}
.seg-item .ico{width:28px;height:28px;margin:8px auto 0;border-radius:50%;background:var(--navy);display:flex;align-items:center;justify-content:center}

.cli-title{left:0;top:762px;width:280px;color:var(--blue);font-size:14px}
.clients{left:10px;top:786px;width:260px;display:flex;align-items:center;justify-content:space-between}
.arrow{width:12px;height:12px;border-radius:50%;background:var(--blue);display:flex;align-items:center;justify-content:center}
.client{width:50px;height:18px;background:var(--light);display:flex;align-items:center;justify-content:center;font-size:5.5px;font-weight:700;color:var(--blue)}

.portfolio{left:0;top:826px;width:280px;height:194px;background:var(--orange);color:#fff}
.port-title{left:0;top:10px;width:280px;font-size:15px}
.port-text{left:60px;top:30px;width:160px;text-align:center;font-size:5.6px;line-height:7.5px}
.grid{left:20px;top:52px;width:240px;display:grid;grid-template-columns:repeat(3,1fr);gap:3px}
.grid div{height:62px}

.con-title{left:0;top:1024px;width:280px;color:var(--blue);font-size:14px}
.con-items{left:16px;top:1046px;width:248px;display:flex;justify-content:space-between}
.con-item{width:56px;text-align:center;font-size:3.8px;line-height:4.8px}
.con-item .ico{width:20px;height:20px;margin:0 auto 3px;border-radius:50%;background:var(--orange);display:flex;align-items:center;justify-content:center}
.form-lead{left:20px;top:1098px;width:240px;text-align:center;font-size:4.2px}
.form{left:20px;top:1110px;width:240px;display:grid;grid-template-columns:1fr 1fr;gap:4px}
.field{height:10px;border:1px solid #d7d7d7;font-size:4px;line-height:8px;padding-left:3px;color:#b0b0b0}
.send{left:200px;top:1156px;width:60px;height:10px;line-height:10px}

.footer{left:0;top:1180px;width:280px;height:20px;background:var(--navy);display:flex;align-items:center;justify-content:center;color:#fff;font-family:"Cabin",sans-serif;font-weight:700;font-size:6px;white-space:nowrap}
</style>
</head>
<body>
<div class="page">

  <div class="abs hero" role="img" aria-label="Foto de equipe de profissionais sorrindo em escritório"></div>
  <div class="abs login">LOGIN</div>
  <div class="abs hero-banner">Somos apaixonados por monitoramento e segurança</div>

  <nav class="abs nav">
    <div class="brand">Trilo Sistemas</div>
    <div class="nav-home">Home</div>
    <div class="nav-links"><span>Soluções</span><span>Segmentos</span><span>Serviços</span><span>Quem Somos</span></div>
  </nav>

  <section class="abs features">
    <div class="feature">
      <div class="thumb" role="img" aria-label="Foto de atendimento ao cliente" style="background:linear-gradient(150deg,#c9cfd3,#7d8a93)"><span class="tag">Atendimento</span></div>
      <p>Equipe pronta para atender sua empresa com agilidade, suporte dedicado e soluções sob medida.</p>
    </div>
    <div class="feature">
      <div class="thumb" role="img" aria-label="Foto de satélite sobre a Terra" style="background:linear-gradient(160deg,#bcd9ee,#4d84b0)"><span class="tag">Telemetria</span></div>
      <p>Telemetria via satélite para acompanhar frotas e equipamentos em qualquer lugar do país.</p>
    </div>
    <div class="feature">
      <div class="thumb" role="img" aria-label="Foto de mãos assinando documento" style="background:linear-gradient(150deg,#eef0f1,#a8b0b6)"><span class="tag">Contratos</span></div>
      <p>Planos flexíveis para empresas e pessoas, com contratos claros e sem surpresas no caminho.</p>
    </div>
  </section>

  <h2 class="abs title sol-title">SOLUÇÕES</h2>
  <p class="abs sol-text">Um <b>sistema</b> que agrega todas as funcionalidades necessárias para <b>gestão de frotas</b>, <b>rastreamento de cargas</b>, <b>valores ou pessoas</b>.</p>
  <div class="abs device" role="img" aria-label="Monitor exibindo o sistema com foto de estrada">
    <div class="screen"></div><div class="stand"></div>
  </div>
  <div class="abs tablet" role="img" aria-label="Tablet exibindo o sistema"></div>
  <div class="abs dots"><span></span><span></span><span></span></div>
  <div class="abs btn sol-btn">Saiba mais</div>

  <section class="abs segments">
    <h2 class="abs title seg-title">SEGMENTOS</h2>
    <p class="abs seg-text">Nossos produtos atendem aos mais <b>diversos segmentos</b>. Veja como podemos <b>alavancar o seu negócio</b>.</p>
    <div class="abs seg-items">
      <div class="seg-item">+ Tecnologia
        <div class="ico"><svg width="14" height="14" viewBox="0 0 14 14"><rect x="3" y="1" width="8" height="12" rx="1" fill="#e5772f"/><rect x="4.5" y="3" width="5" height="6" fill="#fff"/></svg></div>
      </div>
      <div class="seg-item">+ Logística
        <div class="ico"><svg width="14" height="14" viewBox="0 0 14 14"><rect x="1" y="4" width="8" height="6" fill="#e5772f"/><path d="M9 6h3l1 2v2H9z" fill="#e5772f"/><circle cx="4" cy="11" r="1.5" fill="#fff"/><circle cx="11" cy="11" r="1.5" fill="#fff"/></svg></div>
      </div>
      <div class="seg-item">+ Segurança
        <div class="ico"><svg width="14" height="14" viewBox="0 0 14 14"><rect x="3" y="6" width="8" height="7" rx="1" fill="#e5772f"/><path d="M5 6V4a2 2 0 014 0v2" stroke="#e5772f" stroke-width="1.4" fill="none"/></svg></div>
      </div>
    </div>
  </section>

  <h2 class="abs title cli-title">CLIENTES</h2>
  <div class="abs clients">
    <span class="arrow"><svg width="6" height="6" viewBox="0 0 6 6"><path d="M4 1L2 3l2 2" stroke="#fff" fill="none"/></svg></span>
    <span class="client">Fortis</span>
    <span class="client">Norvia</span>
    <span class="client">Cardel</span>
    <span class="client">Lumar</span>
    <span class="arrow"><svg width="6" height="6" viewBox="0 0 6 6"><path d="M2 1l2 2-2 2" stroke="#fff" fill="none"/></svg></span>
  </div>

  <section class="abs portfolio">
    <h2 class="abs title port-title">PORTFÓLIO</h2>
    <p class="abs port-text">Conheça um pouco mais sobre o que fazemos e o que já fizemos.</p>
    <div class="abs grid">
      <div role="img" aria-label="Foto de torre de comunicação" style="background:linear-gradient(#b7c4cc,#55646e)"></div>
      <div role="img" aria-label="Foto de máquinas em mineração" style="background:linear-gradient(#c9b29a,#6a4d33)"></div>
      <div role="img" aria-label="Foto de equipe de executivos" style="background:linear-gradient(#d8dadb,#5b5f63)"></div>
      <div role="img" aria-label="Foto de equipe em reunião" style="background:linear-gradient(#cdd2d5,#4f565b)"></div>
      <div role="img" aria-label="Foto de caminhão na estrada ao entardecer" style="background:linear-gradient(#f0b66a,#5a3b22)"></div>
      <div role="img" aria-label="Foto de instalação industrial iluminada à noite" style="background:linear-gradient(#e79a3c,#3a2a1c)"></div>
    </div>
  </section>

  <h2 class="abs title con-title">CONTATO</h2>
  <div class="abs con-items">
    <div class="con-item"><div class="ico"><svg width="10" height="10" viewBox="0 0 10 10"><rect x="2" y="1" width="6" height="8" fill="#fff"/></svg></div>Solicite uma proposta comercial</div>
    <div class="con-item"><div class="ico"><svg width="10" height="10" viewBox="0 0 10 10"><circle cx="5" cy="5" r="3" fill="#fff"/></svg></div>Fale com o suporte técnico</div>
    <div class="con-item"><div class="ico"><svg width="10" height="10" viewBox="0 0 10 10"><path d="M5 1a3 3 0 013 3c0 2-3 5-3 5S2 6 2 4a3 3 0 013-3z" fill="#fff"/></svg></div>Visite nosso escritório</div>
    <div class="con-item"><div class="ico"><svg width="10" height="10" viewBox="0 0 10 10"><path d="M2 1h2l1 2-1 1a5 5 0 002 2l1-1 2 1v2c-4 0-7-3-7-7z" fill="#fff"/></svg></div>(11) 0000-0000</div>
  </div>
  <p class="abs form-lead">Preencha as informações abaixo que logo retornaremos seu contato.</p>
  <div class="abs form">
    <div class="field">Nome</div><div class="field">Empresa</div>
    <div class="field">E-mail</div><div class="field">Telefone</div>
    <div class="field">Assunto</div><div class="field">Mensagem</div>
  </div>
  <div class="abs btn send">Enviar</div>

  <footer class="abs footer">Trilo Sistemas</footer>
</div>
</body>
</html>
```